Veterinarian specialized in Equine (horse) sports medicine needs logo and stationary design!

New veterinary clinic only focused on horses needs logo and stationary designs. The clinic works with sport horses including jumping horses, dressage horses and polo horses (all disciplines you can find online. No racing horses). Name of clinic is StrideCare and is based in Mexico City where there is a large and elite clientele of sports horses. My main focus is orthopedics and rehabilitation.
I think logo should include horse(s), especially if they are performing a sport (like jumping, etc).

Target Market(s)

Elite horse-owners of sport horses.

Industry/Entity Type

Horseback Riding

Requirements
Must have
• Great Logo! I like bold and bright colors (no pastels), but with a professional tone.

```html
<!DOCTYPE html>
<html lang="en">
<head>
<meta charset="utf-8">
<title>StrideCare Stationery Set</title>
<link href="https://fonts.googleapis.com/css2?family=PT+Serif:wght@700&family=Open+Sans:wght@400;700&display=swap" rel="stylesheet">
<style>
  :root {
    --backdrop: #c2b49a;
    --paper: #ffffff;
    --paper-textured: #eeeff2;
    --brand-blue: #1e4aa0;
    --brand-blue-deep: #1a3f8c;
    --brand-red: #e2262b;
    --ink: #333333;
    --ink-soft: #555555;
    --serif: "PT Serif", Georgia, serif;
    --sans: "Open Sans", Arial, sans-serif;
  }
  * { box-sizing: border-box; margin: 0; padding: 0; }
  html, body { width: 1200px; height: 1200px; overflow: hidden; }
  body { background: var(--backdrop); position: relative; font-family: var(--sans); color: var(--ink); }

  .sheet { position: absolute; background: var(--paper); overflow: hidden; }
  .textured-fill { position: absolute; inset: 0; background: var(--paper-textured); }

  .wordmark {
    font-family: var(--serif); font-weight: 700; color: var(--ink);
    display: flex; align-items: center; gap: 5px; white-space: nowrap; line-height: 1;
  }
  .wordmark .dot { border-radius: 50%; background: var(--brand-blue); flex: none; }
  .wordmark.on-blue { color: #ffffff; }
  .wordmark.on-blue .dot { background: #ffffff; }

  .contact { font-size: 5px; line-height: 1.45; color: var(--ink-soft); }

  /* Large envelope */
  .envelope-large { left: 46px; top: 72px; width: 259px; height: 365px; }
  .envelope-large .flap {
    position: absolute; left: 0; top: 0; width: 100%; height: 44px;
    background: var(--brand-blue); border-radius: 0 0 10px 10px;
    display: flex; justify-content: center; align-items: center;
  }
  .envelope-large .contact { position: absolute; left: 26px; bottom: 22px; }

  /* Plain letter */
  .letter-plain { left: 319px; top: 72px; width: 258px; height: 365px; }
  .letter-plain .lockup { position: absolute; right: 22px; bottom: 27px; text-align: right; }
  .letter-plain .contact { margin-top: 4px; }

  /* Letterhead */
  .letterhead { left: 614px; top: 72px; width: 258px; height: 365px; }
  .letterhead .masthead { position: absolute; top: 20px; left: 0; width: 100%; display: flex; flex-direction: column; align-items: center; gap: 5px; }
  .letterhead .salutation { position: absolute; top: 88px; left: 37px; font-size: 4.5px; line-height: 1.4; }
  .letterhead .salutation b { font-size: 5px; }
  .letterhead .date { position: absolute; top: 88px; right: 38px; font-size: 5px; font-weight: 700; }
  .letterhead .body-copy { position: absolute; top: 112px; left: 37px; right: 38px; font-size: 4.1px; line-height: 1.3; color: var(--ink-soft); text-align: justify; }
  .letterhead .body-copy p { margin-bottom: 6px; }
  .letterhead .sign-off { position: absolute; top: 289px; left: 37px; font-size: 4.5px; line-height: 1.4; }
  .letterhead .sign-off b { font-size: 5.5px; }
  .letterhead .signature { width: 40px; height: 9px; margin-top: 4px; background: #d8d8d8; border-radius: 2px; }
  .letterhead .rule { position: absolute; top: 335px; left: 37px; right: 38px; height: 1px; background: var(--brand-red); }
  .letterhead .rule-accent { position: absolute; top: 334px; left: 97px; width: 58px; height: 2px; background: var(--brand-blue); }
  .footer-contacts { display: flex; gap: 14px; align-items: center; font-size: 3.5px; color: var(--ink-soft); }
  .footer-contacts span { display: flex; align-items: center; gap: 3px; }
  .letterhead .footer-contacts { position: absolute; top: 346px; left: 0; width: 100%; justify-content: center; }

  /* Spiral notepad */
  .notepad { left: 918px; top: 160px; width: 202px; height: 277px; }
  .notepad-coil { position: absolute; left: 940px; top: 156px; width: 170px; height: 16px; display: flex; justify-content: space-between; }
  .notepad-coil i { width: 3.5px; height: 16px; background: var(--brand-blue); border-radius: 2px; display: block; }
  .notepad .lockup { position: absolute; top: 152px; left: 0; width: 100%; display: flex; justify-content: center; }
  .notepad .base-rule { position: absolute; left: 18px; right: 11px; top: 263px; height: 1.5px; background: var(--brand-red); }
  .notepad .url-tab { position: absolute; left: 75px; top: 261px; width: 54px; height: 6px; background: var(--brand-blue); color: #fff; font-size: 3.5px; text-align: center; line-height: 6px; }

  /* Ring notebook */
  .notebook { left: 102px; top: 524px; width: 253px; height: 357px; }
  .notebook-rings { position: absolute; left: 85px; top: 541px; width: 32px; height: 320px; display: flex; flex-direction: column; justify-content: space-between; }
  .notebook-rings i { display: block; width: 31px; height: 7px; background: var(--brand-blue); border-radius: 4px; border-right: 3px solid #c8a06a; }
  .notebook .lockup { position: absolute; right: 22px; top: 266px; text-align: right; display: flex; flex-direction: column; align-items: flex-end; gap: 4px; }
  .notebook .contact { font-size: 5px; }

  /* Presentation folder */
  .folder-inside { position: absolute; left: 426px; top: 498px; width: 316px; height: 364px; background: var(--brand-blue); clip-path: polygon(13% 0, 100% 0, 100% 100%, 0 100%, 0 7%); }
  .folder-inside .footer-contacts { position: absolute; left: 110px; top: 342px; color: #dfe6f5; font-size: 3.5px; }
  .folder-pocket { position: absolute; left: 478px; top: 862px; width: 264px; height: 62px; }
  .folder-front { left: 742px; top: 498px; width: 266px; height: 364px; }
  .folder-front .lockup { position: absolute; top: 207px; left: 0; width: 100%; display: flex; justify-content: center; }

  /* DL envelopes */
  .envelope-window { left: 244px; top: 984px; width: 281px; height: 141px; }
  .envelope-window .window { position: absolute; left: 21px; top: 73px; width: 96px; height: 48px; border-radius: 7px; background: linear-gradient(135deg, #2b58b5, var(--brand-blue-deep)); }
  .envelope-window .lockup { position: absolute; right: 13px; top: 80px; display: flex; flex-direction: column; align-items: flex-end; gap: 4px; }
  .envelope-window .contact { text-align: right; }
  .envelope-back { left: 544px; top: 984px; width: 281px; height: 141px; }
  .envelope-back .flap { position: absolute; left: 0; top: 0; width: 100%; height: 46px; background: var(--brand-blue); border-radius: 0 0 10px 10px; display: flex; justify-content: center; align-items: center; }
</style>
</head>
<body>

  <!-- Large envelope -->
  <div class="sheet envelope-large">
    <div class="flap">
      <div class="wordmark on-blue" style="font-size:13px"><span class="dot" style="width:7px;height:7px"></span>StrideCare</div>
    </div>
    <div class="contact">555-210-4870<br>48 Calle Arenal, Mexico City 11000<br>www.stridecare.vet</div>
  </div>

  <!-- Plain letter -->
  <div class="sheet letter-plain">
    <div class="lockup">
      <div class="wordmark" style="font-size:12px;justify-content:flex-end"><span class="dot" style="width:7px;height:7px"></span>StrideCare</div>
      <div class="contact">48 Calle Arenal, Mexico City 11000</div>
    </div>
  </div>

  <!-- Letterhead -->
  <div class="sheet letterhead">
    <div class="masthead">
      <div class="wordmark" style="font-size:11px"><span class="dot" style="width:6px;height:6px"></span>StrideCare</div>
      <div class="contact" style="font-size:4.5px">48 Calle Arenal, Mexico City 11000</div>
    </div>
    <div class="salutation"><b>Dear, Mr________</b><br>Designation<br>COMPANY NAME</div>
    <div class="date">DATE:1/5/2018</div>
    <div class="body-copy">
      <p>Thank you for trusting our team with the care of your horse. This letter summarises the orthopedic review, the imaging results and the rehabilitation plan agreed at the last visit. We will follow up with a progress check in two weeks and adjust the exercise schedule as needed.</p>
      <p>Thank you for trusting our team with the care of your horse. This letter summarises the orthopedic review, the imaging results and the rehabilitation plan agreed at the last visit. We will follow up with a progress check in two weeks and adjust the exercise schedule as needed.</p>
      <p>Thank you for trusting our team with the care of your horse. This letter summarises the orthopedic review, the imaging results and the rehabilitation plan agreed at the last visit. We will follow up with a progress check in two weeks and adjust the exercise schedule as needed.</p>
      <p>Thank you for trusting our team with the care of your horse. This letter summarises the orthopedic review, the imaging results and the rehabilitation plan agreed at the last visit. We will follow up with a progress check in two weeks and adjust the exercise schedule as needed.</p>
    </div>
    <div class="sign-off"><b>YOUR NAME</b><br>Designation
      <div class="signature" role="img" aria-label="Handwritten signature"></div>
    </div>
    <div class="rule"></div>
    <div class="rule-accent"></div>
    <div class="footer-contacts">
      <span><svg width="5" height="5" viewBox="0 0 10 10"><path d="M2 1l2 2-1 1.5a6 6 0 0 0 2.5 2.5L7 6l2 2-1.5 1.5C4 9 1 6 .5 2.5z" fill="#555"/></svg>555-210-4870</span>
      <span><svg width="5" height="4" viewBox="0 0 10 8"><rect x=".5" y=".5" width="9" height="7" fill="none" stroke="#555"/><path d="M.5 .5l4.5 4 4.5-4" fill="none" stroke="#555"/></svg>hello@stridecare.vet</span>
      <span><svg width="5" height="5" viewBox="0 0 10 10"><circle cx="5" cy="5" r="4.5" fill="none" stroke="#555"/><path d="M.5 5h9M5 .5c-3 3-3 6 0 9M5 .5c3 3 3 6 0 9" fill="none" stroke="#555"/></svg>www.stridecare.vet</span>
    </div>
  </div>

  <!-- Spiral notepad -->
  <div class="sheet notepad">
    <div class="textured-fill" role="img" aria-label="Light grey chevron paper texture"></div>
    <div class="lockup">
      <div class="wordmark" style="font-size:14px"><span class="dot" style="width:8px;height:8px"></span>StrideCare</div>
    </div>
    <div class="base-rule"></div>
    <div class="url-tab">www.stridecare.vet</div>
  </div>
  <div class="notepad-coil">
    <i></i><i></i><i></i><i></i><i></i><i></i><i></i><i></i><i></i><i></i><i></i><i></i><i></i><i></i><i></i><i></i><i></i><i></i>
  </div>

  <!-- Ring notebook -->
  <div class="sheet notebook">
    <div class="textured-fill" role="img" aria-label="Light grey chevron paper texture"></div>
    <div class="lockup">
      <div class="wordmark" style="font-size:12px"><span class="dot" style="width:7px;height:7px"></span>StrideCare</div>
      <div class="contact" style="text-align:right">555-210-4870<br>hello@stridecare.vet<br>48 Calle Arenal, Mexico City 11000<br>www.stridecare.vet</div>
    </div>
  </div>
  <div class="notebook-rings">
    <i></i><i></i><i></i><i></i><i></i><i></i><i></i><i></i><i></i><i></i><i></i><i></i><i></i><i></i>
  </div>

  <!-- Presentation folder -->
  <div class="folder-inside">
    <div class="footer-contacts">
      <span><svg width="5" height="5" viewBox="0 0 10 10"><path d="M2 1l2 2-1 1.5a6 6 0 0 0 2.5 2.5L7 6l2 2-1.5 1.5C4 9 1 6 .5 2.5z" fill="#fff"/></svg>555-210-4870</span>
      <span><svg width="5" height="4" viewBox="0 0 10 8"><rect x=".5" y=".5" width="9" height="7" fill="none" stroke="#fff"/><path d="M.5 .5l4.5 4 4.5-4" fill="none" stroke="#fff"/></svg>hello@stridecare.vet</span>
      <span><svg width="5" height="5" viewBox="0 0 10 10"><circle cx="5" cy="5" r="4.5" fill="none" stroke="#fff"/><path d="M.5 5h9M5 .5c-3 3-3 6 0 9M5 .5c3 3 3 6 0 9" fill="none" stroke="#fff"/></svg>www.stridecare.vet</span>
    </div>
  </div>
  <svg class="folder-pocket" viewBox="0 0 264 62" aria-hidden="true">
    <polygon points="0,0 264,0 264,5 210,62 0,62" fill="#1d49a0"/>
  </svg>
  <div class="sheet folder-front">
    <div class="textured-fill" role="img" aria-label="Light grey chevron paper texture"></div>
    <div class="lockup">
      <div class="wordmark" style="font-size:24px;gap:8px"><span class="dot" style="width:13px;height:13px"></span>StrideCare</div>
    </div>
  </div>

  <!-- Window envelope -->
  <div class="sheet envelope-window">
    <div class="window"></div>
    <div class="lockup">
      <div class="wordmark" style="font-size:12px"><span class="dot" style="width:7px;height:7px"></span>StrideCare</div>
      <div class="contact">555-210-4870<br>48 Calle Arenal, Mexico City 11000<br>www.stridecare.vet</div>
    </div>
  </div>

  <!-- Envelope back -->
  <div class="sheet envelope-back">
    <div class="flap">
      <div class="wordmark on-blue" style="font-size:13px"><span class="dot" style="width:7px;height:7px"></span>StrideCare</div>
    </div>
  </div>

</body>
</html>
```